Business Card Design

Business Card for professional consulting firm working with large financial institutions.

Target Market(s)

Executive buyers

Industry/Entity Type

Banking

Contact Information for Business Card

Mild creativity wanted. Not boring, but do elaborate artwork.

Font styles to use
Serif
Sans Serif

Colors

Designer to choose colors to be used in the design.

Requirements
Must have
• Standard business card features - company name, individual name, telephone, website, email, locations.
Nice to have
• Two colors
Should not have
• too many colors, fancy printing, cartoons.

```html
<!DOCTYPE html>
<html lang="en">
<head>
<meta charset="UTF-8">
<title>k7advisory Business Card</title>
<link href="https://fonts.googleapis.com/css2?family=Roboto:wght@400;500;700&display=swap" rel="stylesheet">
<style>
  :root {
    --backdrop: #5b5b5d;
    --card: #333335;
    --card-edge: #2b2b2d;
    --gold: #c9ab6b;
    --text-light: #e6e6e6;
    --logo-grey: #8a8a8d;
  }
  * { margin: 0; padding: 0; box-sizing: border-box; }
  html, body {
    width: 1200px;
    height: 1000px;
    overflow: hidden;
  }
  body {
    background: var(--backdrop);
    font-family: "Roboto", Arial, sans-serif;
    position: relative;
  }
  .card {
    position: absolute;
    width: 600px;
    height: 343px;
    background: var(--card);
    border: 1px solid var(--card-edge);
    border-radius: 24px;
    box-shadow: 0 10px 30px rgba(0,0,0,0.35);
  }
  .card--front { left: 530px; top: 90px; }
  .card--back { left: 80px; top: 480px; }

  .brand {
    position: absolute;
    right: 52px;
    bottom: 62px;
    display: flex;
    align-items: center;
    gap: 12px;
    color: var(--logo-grey);
    font-size: 40px;
    font-weight: 400;
  }
  .brand__dot {
    width: 14px;
    height: 14px;
    border-radius: 50%;
    background: var(--logo-grey);
  }

  .person {
    position: absolute;
    left: 40px;
    top: 40px;
  }
  .person__name {
    color: var(--gold);
    font-size: 24px;
    font-weight: 700;
    letter-spacing: 0.5px;
  }
  .person__title {
    color: var(--text-light);
    font-size: 14px;
    margin-top: 2px;
  }

  .contact {
    position: absolute;
    left: 40px;
    bottom: 34px;
    right: 36px;
    color: var(--text-light);
    font-size: 14.5px;
    line-height: 1.7;
  }
  .contact__address { margin-bottom: 4px; }
  .contact__row {
    display: flex;
    align-items: center;
    gap: 9px;
  }
  .contact__row svg { width: 14px; height: 14px; fill: var(--gold); flex: none; }
  .contact__web {
    position: absolute;
    right: 0;
    bottom: 0;
  }
  .contact__web strong { color: var(--gold); font-weight: 500; }
</style>
</head>
<body>

  <section class="card card--front" aria-label="Card front">
    <div class="brand">
      <span class="brand__dot"></span>
      <span class="brand__name">k7advisory</span>
    </div>
  </section>

  <section class="card card--back" aria-label="Card back">
    <div class="person">
      <div class="person__name">DANIEL HARPER</div>
      <div class="person__title">General Manager</div>
    </div>

    <div class="contact">
      <div class="contact__address">48 W Meridian Street Halden Tower 12th Floor Phoenix, Arizona 85003</div>
      <div class="contact__row">
        <svg viewBox="0 0 24 24" aria-hidden="true"><path d="M6.6 10.8a15.1 15.1 0 0 0 6.6 6.6l2.2-2.2a1 1 0 0 1 1-.25 11.4 11.4 0 0 0 3.6.57 1 1 0 0 1 1 1V20a1 1 0 0 1-1 1A17 17 0 0 1 3 4a1 1 0 0 1 1-1h3.5a1 1 0 0 1 1 1c0 1.25.2 2.45.57 3.57a1 1 0 0 1-.25 1z"/></svg>
        <span>+602-555-0147</span>
      </div>
      <div class="contact__row">
        <svg viewBox="0 0 24 24" aria-hidden="true"><path d="M2 5h20v14H2z M4 7v.5l8 5 8-5V7l-8 5z" fill-rule="evenodd"/></svg>
        <span>info@k7advisory.us</span>
      </div>
      <div class="contact__row contact__web">
        <svg viewBox="0 0 24 24" aria-hidden="true"><path d="M12 2a10 10 0 1 0 0 20 10 10 0 0 0 0-20zm6.9 6h-3a15 15 0 0 0-1.4-4 8 8 0 0 1 4.4 4zM12 4a13 13 0 0 1 1.9 4h-3.8A13 13 0 0 1 12 4zM4.3 14a8 8 0 0 1 0-4h3.4a16 16 0 0 0 0 4zm.8 2h3a15 15 0 0 0 1.4 4 8 8 0 0 1-4.4-4zm3-8h-3a8 8 0 0 1 4.4-4 15 15 0 0 0-1.4 4zM12 20a13 13 0 0 1-1.9-4h3.8A13 13 0 0 1 12 20zm2.3-6H9.7a14 14 0 0 1 0-4h4.6a14 14 0 0 1 0 4zm.2 6a15 15 0 0 0 1.4-4h3a8 8 0 0 1-4.4 4zm1.8-6a16 16 0 0 0 0-4h3.4a8 8 0 0 1 0 4z"/></svg>
        <span>www.<strong>k7advisory</strong>.us</span>
      </div>
    </div>
  </section>

</body>
</html>
```